R J Penn Accounting & SMSF Auditing needs a Web Site Design

I need some examples of what a web design can look like for my business.
The business name is above and I have already registered a domain name of www.penn-smsf.com.au
I have attached my current letterhead and business cards and would like to maintain these colours basically Red on White with some black

Industry/Entity Type

Business

```html
<!DOCTYPE html>
<html lang="en">
<head>
<meta charset="utf-8">
<title>R J Penn Accounting &amp; SMSF Auditing</title>
<link rel="stylesheet" href="https://fonts.googleapis.com/css2?family=Mulish:wght@300;400;600;700;800&display=swap">
<style>
:root{
  --red:#c8081c;
  --ink:#222222;
  --topbar:#1e1e1e;
  --white:#ffffff;
  --grey-bg:#f2f2f2;
  --rule:#d8d8d8;
  --muted:#555555;
}
*{box-sizing:border-box;margin:0;padding:0}
html,body{width:1003px;height:1200px;overflow:hidden}
body{font-family:"Mulish",Arial,sans-serif;color:var(--ink);background:var(--white);position:relative}
.topbar{position:absolute;left:0;top:0;width:1003px;height:35px;background:var(--topbar);color:var(--white);font-size:11.5px}
.topbar .contact{position:absolute;right:95px;top:0;height:35px;display:flex;align-items:center;gap:10px}
.topbar .item{display:flex;align-items:center;gap:5px}
.topbar .phone{font-size:12.5px}
.header{position:absolute;left:0;top:35px;width:1003px;height:84px;background:var(--red);color:var(--white)}
.brand{position:absolute;left:92px;top:12px}
.brand .name{font-weight:700;font-size:18.5px;line-height:21px;letter-spacing:-.2px}
.brand .name span{display:block;font-size:21px}
.brand .sub{font-size:7.5px;letter-spacing:4.2px;margin-top:6px}
.nav{position:absolute;left:415px;top:0;height:74px;display:flex;align-items:center;gap:18px;font-size:14.5px;font-weight:600}
.quote{position:absolute;left:785px;top:22px;width:123px;height:35px;background:var(--white);color:var(--ink);font-size:11.5px;font-weight:700;display:flex;align-items:center;justify-content:center;border-radius:2px}
.hero{position:absolute;left:0;top:119px;width:1003px;height:439px;background:linear-gradient(180deg,#b9cde6 0%,#8ea6c6 30%,#1e2538 55%,#2a3040 72%,#e4e6ea 88%,#f3f3f4 100%)}
.hero .arrow{position:absolute;top:204px}
.welcome{position:absolute;left:92px;top:600px;width:450px}
.welcome h1{color:var(--red);font-weight:800;line-height:1}
.welcome h1 .small{display:block;font-size:23px;letter-spacing:-.3px}
.welcome h1 .big{display:block;font-size:43px;margin-top:6px;letter-spacing:-.5px}
.copy{font-size:14px;line-height:28.4px;color:var(--ink);letter-spacing:-.3px}
.welcome .copy{margin-top:56px}
.profile{position:absolute;left:577px;top:606px;width:330px;height:350px;border:1px solid var(--rule);box-shadow:0 1px 3px rgba(0,0,0,.12);background:var(--white);padding:14px 8px 0 19px}
.profile h2{color:var(--red);font-size:23px;font-weight:800;margin-left:4px}
.profile .role{font-size:19px;line-height:30px;margin-left:4px;margin-top:2px}
.profile .copy{margin-top:16px}
.partners{position:absolute;left:92px;top:1010px;width:816px;height:75px;display:flex;justify-content:space-between;align-items:center}
.partner{font-size:16px;font-weight:700;color:var(--muted)}
.footer{position:absolute;left:0;top:1122px;width:1003px;height:78px;background:var(--grey-bg);font-size:12px}
.footer .links{position:absolute;left:92px;top:16px;display:flex;gap:9px}
.footer .links .sep{color:#777}
.footer .copyright{position:absolute;left:92px;top:45px}
.member{position:absolute;left:778px;top:26px;display:flex;align-items:center;gap:7px;font-size:11px;font-weight:600;color:var(--muted)}
.member .badge{width:24px;height:24px;border-radius:50%;border:1.5px solid #777}
</style>
</head>
<body>
<div class="topbar">
  <div class="contact">
    <div class="item">
      <svg width="16" height="11" viewBox="0 0 16 11"><rect x=".5" y=".5" width="15" height="10" fill="none" stroke="#fff"/><path d="M.5 .5 8 6.5 15.5 .5" fill="none" stroke="#fff"/></svg>
      <span>rjpenn@mailhub.net.au</span>
    </div>
    <div class="item phone">
      <svg width="15" height="15" viewBox="0 0 15 15"><circle cx="7.5" cy="7.5" r="7.5" fill="#fff"/><path d="M5 3.8c.4-.3.8-.2 1 .2l.6 1.2c.2.4 0 .7-.3 1l-.4.3c.4.9 1.1 1.6 2 2l.3-.4c.3-.3.6-.4 1-.2l1.2.6c.4.2.5.6.2 1-.6.8-1.4 1-2.4.6A6.2 6.2 0 0 1 4.4 6.2c-.3-1 0-1.8.6-2.4z" fill="#1e1e1e"/></svg>
      <span>0400 123 456</span>
    </div>
  </div>
</div>

<header class="header">
  <div class="brand">
    <div class="name">R J Penn Accounting<span>&amp; SMSF Auditing</span></div>
    <div class="sub">HALDEN PENN PTY LTD</div>
  </div>
  <nav class="nav">
    <span>Home</span><span>About Us</span><span>Services</span><span>FAQ’s</span><span>Contact Us</span>
  </nav>
  <div class="quote">REQUEST A QUOTE</div>
</header>

<section class="hero" role="img" aria-label="Photo of an accountant in a blue shirt and tie using a calculator over paperwork and a laptop">
  <svg class="arrow" style="left:76px" width="18" height="28" viewBox="0 0 18 28"><path d="M14 3 4 14l10 11" fill="none" stroke="#fff" stroke-width="3.5"/></svg>
  <svg class="arrow" style="left:906px" width="18" height="28" viewBox="0 0 18 28"><path d="M4 3l10 11L4 25" fill="none" stroke="#fff" stroke-width="3.5"/></svg>
</section>

<section class="welcome">
  <h1><span class="small">Welcome to R J Penn Accounting</span><span class="big">&amp; SMSF Auditing</span></h1>
  <p class="copy">Sed ut perspiciatis unde omnis iste natus error sit voluptatem accusantium doloremque laudantium, totam rem aperiam, eaque ipsa quae ab illo inventore veritatis et quasi architecto beatae vitae dicta sunt explicabo. Nemo enim ipsam voluptatem quia voluptas sit aspernatur aut odit aut fugit, sed quia consequuntur magni dolores eos qui ratione voluptatem sequi nesciunt. Neque porro quisquam est, qui dolorem ipsum quia dolor sit amet, consectetur, adipisci velit, sed quia non numquam eius modi tempora incidunt .</p>
</section>

<aside class="profile">
  <h2>Robert J. Penn</h2>
  <p class="role">Director :&nbsp; FGPA AFMI<br>FSRC SMSF Registered Auditor</p>
  <p class="copy">Sed ut perspiciatis unde omnis iste natus error sit voluptatem accusantium doloremque laudantium, totam rem aperiam, eaque ipsa quae ab illo inventore veritatis et quasi architecto beatae vitae dicta sunt explicabo. Nemo enim ipsam voluptatem quia voluptas sit aspernatur aut odit aut fugit, sed quia consequuntur</p>
</aside>

<section class="partners">
  <div class="partner">Northgate Audit</div>
  <div class="partner">Tallis Advisory</div>
  <div class="partner">Kestrel Partners</div>
  <div class="partner">Brindle &amp; Co</div>
  <div class="partner">Ardent Auditing</div>
</section>

<footer class="footer">
  <div class="links">
    <span>Home</span><span class="sep">|</span><span>About Us</span><span class="sep">|</span><span>Services</span><span class="sep">|</span><span>FAQ’s</span><span class="sep">|</span><span>Contact Us</span>
  </div>
  <div class="copyright">© 2014 Company Name ,All Rights Reserved</div>
  <div class="member"><span class="badge"></span>Guild of Public Accountants</div>
</footer>
</body>
</html>
```